Banner Pop Up Opt In Form REDESIGNS - SLEEK BLACK LOOK

Please redesign banners attached.

I am looking for a very sleek look....I do not like this collage of images on these current designs. Please keep all content same but use images that pop.

I have an acccount at www.pixmorrow-example.com or you can use your own images.

I like black background for somereason because it looks very sleek....but these designs should pop , build trust and credibility and have easy opt in form....SLEEK AND MODERN LOOK is what im looking for....

Target Market(s)

Consumers on websites

Requirements
Must have
• Please redesign banners attached.

Nice to have

Should not have

```html
<!DOCTYPE html>
<html lang="en">
<head>
<meta charset="UTF-8">
<title>Newsletter Offer Banner</title>
<link href="https://fonts.googleapis.com/css2?family=Open+Sans:wght@300;400;600;700&display=swap" rel="stylesheet">
<style>
  :root {
    --lime: #b7c91b;
    --field: #d9efff;
    --panel: rgba(24, 32, 36, 0.66);
    --white: #ffffff;
    --ice: #d6ecff;
    --ink: #111111;
    --field-border: #3b4a50;
    --scene-deep: #1d3a44;
    --scene-water: #3f8d98;
    --scene-sand: #b9bfae;
    --scene-green: #2e4d39;
    --scene-dark: #16231c;
  }
  * { box-sizing: border-box; margin: 0; padding: 0; }
  html, body { width: 1200px; height: 1032px; overflow: hidden; }
  body { font-family: "Open Sans", Arial, sans-serif; background: #141c1f; }

  .banner { position: relative; width: 1200px; height: 1032px; overflow: hidden; }

  .beach-scene {
    position: absolute; inset: 0;
    background: linear-gradient(165deg,
      var(--scene-deep) 0%,
      var(--scene-water) 40%,
      var(--scene-sand) 62%,
      var(--scene-green) 84%,
      var(--scene-dark) 100%);
  }

  .offer-panel {
    position: absolute; left: 0; top: 0; width: 718px; height: 1032px;
    background: var(--panel);
  }

  .accent-bar {
    position: absolute; left: 186px; width: 338px; height: 14px;
    background: var(--lime);
  }
  .accent-bar.top { top: 0; }
  .accent-bar.bottom { bottom: 0; }

  .headline {
    position: absolute; left: 0; width: 718px; top: 118px;
    text-align: center; color: var(--white);
    font-weight: 400; font-size: 70px; line-height: 80px;
    letter-spacing: 1px;
  }
  .subhead {
    position: absolute; left: 0; width: 718px; top: 293px;
    text-align: center; color: var(--white);
    font-weight: 700; font-size: 25px; line-height: 30px;
  }
  .certificate {
    position: absolute; left: 0; width: 718px; top: 404px;
    text-align: center; color: var(--ice);
    font-weight: 700; font-size: 33px; line-height: 40px;
    letter-spacing: 0.5px;
  }

  .optin-form { position: absolute; left: 68px; top: 538px; width: 575px; }
  .optin-field {
    display: block; width: 575px; height: 86px; margin-bottom: 7px;
    background: var(--field); border: 2px solid var(--field-border);
    padding: 0 26px; font-family: inherit; font-size: 33px; color: var(--ink);
  }
  .optin-field::placeholder { color: var(--ink); }
  .submit-button {
    display: block; width: 575px; height: 86px;
    background: var(--lime); border: none;
    font-family: inherit; font-weight: 700; font-size: 33px; color: var(--ink);
    letter-spacing: 0.5px;
  }

  .fine-print {
    position: absolute; left: 0; width: 718px; top: 928px;
    text-align: center; color: var(--white);
    font-size: 22px; line-height: 27px;
  }
</style>
</head>
<body>
<div class="banner">
  <div class="beach-scene" role="img" aria-label="Aerial photo of a tropical beach lagoon with palm trees, white sand and turquoise water"></div>

  <section class="offer-panel">
    <div class="accent-bar top"></div>
    <h1 class="headline">WANT A<br>GREAT OFFER?</h1>
    <p class="subhead">SUBSCRIBE TO OUR NEWSLETTER AND<br>RECEIVE A COMPLIMENTARY</p>
    <p class="certificate">$300 RESTAURANT CERTIFICATE</p>

    <form class="optin-form">
      <input class="optin-field" type="text" placeholder="Name">
      <input class="optin-field" type="email" placeholder="Email">
      <input class="optin-field" type="tel" placeholder="Phone">
      <button class="submit-button" type="button">SUBMIT</button>
    </form>

    <p class="fine-print">We will send an email and text message<br>with the offer and instructions on how to redeem.</p>
    <div class="accent-bar bottom"></div>
  </section>
</div>
</body>
</html>
```